Website Redesign for Allies of Beit Noam

Beit Noam's mission is to enable chronically ill, disabled, infirm, and terminally ill people in Israel to live with dignity. Allies of Beit Noam raises awareness of and funds for Beit Noam to its friends in the USA. This project is to redesign Allies of Beit Noam's current site (https://alliesofbeitnoam.org/).

The redesigned site will use current colors, logo, and text, but will get new images. The design must 1) project a friendlier vibe, 2) be emotionally engaging and inviting (so people will make donations), and 3) be clear (so people get an understanding of Beit Noam at a glance).

Please provide a homepage design and one inner page design.
Please provide PSD files so we can see all layers of the design.
Please take the colors from the current logo.

Target Market(s)

high net worth individuals who are interested in Israel, Jewish causes, philanthropic elder care and medical care.

Industry/Entity Type

non-profit fundraising organization for old and young in Israel who are chronically ill, disabled, infirm, and terminally ill.

Number of Pages Required

2 page

Font styles to use
Sans Serif

Colors
0054AA
0677BA
7BADD7
CADEEF
E8F1F8
EB3D1F
EC4F4E
F09395
F8D3D4
FCEDEE

Requirements
Must have
• PSD files. site colors from logo (red and blue). friendly, emotionally engaging and clear so people will donate.
Should not have
• not too flashy - target market is older

```html
<!DOCTYPE html>
<html lang="en">
<head>
<meta charset="utf-8">
<title>Allies of Beit Noam – Homepage Design</title>
<link href="https://fonts.googleapis.com/css2?family=Roboto:wght@400;500;700&display=swap" rel="stylesheet">
<style>
:root{
  --blue:#2637a3;
  --blue-deep:#1a2a92;
  --navy:#0b1a7f;
  --title:#2b2f7a;
  --red:#d8232a;
  --red-text:#e2302d;
  --ink:#444;
  --soft:#ece4ef;
  --pink:#f5e0e6;
  --white:#fff;
}
*{margin:0;padding:0;box-sizing:border-box}
html,body{width:1200px;height:877px;overflow:hidden;background:#fff;font-family:"Roboto",Arial,sans-serif;color:var(--ink)}
.canvas{position:relative;width:1200px;height:877px;overflow:hidden;background:#fff}
.a{position:absolute}
.photo{position:absolute}
.btn-red{position:absolute;background:var(--red);color:#fff;font-weight:500;display:flex;align-items:center;justify-content:center;text-transform:uppercase}
.btn-line{position:absolute;border:1px solid var(--red-text);color:var(--red-text);background:#fff;display:flex;align-items:center;justify-content:center}
.center{text-align:center}

/* left panel */
.help-band{left:38px;top:10px;width:665px;height:319px;background:linear-gradient(120deg,#2a3ba6,#3647b0 50%,#2434a0)}
.brand-box{left:38px;top:12px;width:127px;height:51px;background:#fff;display:flex;align-items:center;gap:6px;padding-left:6px}
.brand-box .dot{width:20px;height:20px;border-radius:50%;background:var(--red);flex:none}
.brand-box span{font-weight:700;font-size:12px;color:var(--title);line-height:1.1}
.band-title{color:#fff;font-size:16px;font-weight:500;letter-spacing:.3px}
.help-card{position:absolute;background:rgba(255,255,255,.72)}
.help-card.active{background:#fff;box-shadow:0 2px 8px rgba(0,0,0,.25)}
.help-card p{font-size:10px;line-height:13px;color:#555;text-align:center}
.help-card .price{color:var(--red);font-weight:700;font-size:13px;text-align:center}
.dots{left:302px;top:308px;display:flex;gap:4px;align-items:center}
.dots i{width:5px;height:5px;border-radius:50%;background:rgba(255,255,255,.6)}
.dots i.on{width:8px;height:8px;background:#fff}

.impact-zone{left:38px;top:329px;width:665px;height:548px;background:linear-gradient(135deg,#e6e2f0,#f4dfe6 70%,#f2dbe2)}
.sec-title{color:var(--title);font-weight:700;font-size:16px}
.impact-card{position:absolute;top:400px;width:166px;height:225px;background:#fff;border:1px solid #ddd}
.impact-card .date{position:absolute;left:13px;top:119px;font-size:8px;color:#555}
.impact-card h3{position:absolute;left:13px;top:133px;font-size:10px;font-weight:500;color:var(--red-text)}
.impact-card p{position:absolute;left:13px;top:146px;width:142px;font-size:8px;line-height:11px;color:#444}
.news h3{font-size:10px;font-weight:500;color:var(--red-text)}
.news .date{font-size:8px;color:#555}
.news p{font-size:8px;line-height:12px;color:#444}

/* right panel */
.stats-band{left:703px;top:10px;width:477px;height:200px;background:linear-gradient(120deg,#2435a0,#3244ad)}
.stat{position:absolute;top:90px;width:80px;text-align:center;color:#fff}
.stat .ring{width:40px;height:40px;border-radius:50%;border:1.5px solid rgba(255,255,255,.85);margin:0 auto 6px;display:flex;align-items:center;justify-content:center}
.stat b{display:block;font-size:11px;font-weight:500}
.stat small{display:block;font-size:8px;line-height:9px}
.info-zone{left:703px;top:210px;width:477px;height:435px;background:linear-gradient(180deg,#e8e8f3,#f1e3ea)}
.body-text{font-size:9.5px;line-height:13px;color:#444}
.footer{left:703px;top:645px;width:477px;height:232px;background:var(--navy);color:#fff}
.foot-nav{left:934px;top:685px;width:180px;font-size:8.5px;line-height:15px;white-space:nowrap}
.foot-nav a{color:#fff;text-decoration:none;font-size:8.5px;font-weight:500;margin-right:9px}
.social{position:absolute;top:732px;width:17px;height:17px;border-radius:50%;border:1px solid #fff;display:flex;align-items:center;justify-content:center}
.social::after{content:"";width:5px;height:5px;border-radius:50%;background:#fff}

/* mini page */
.mini{left:513px;top:27px;width:190px;height:835px;background:#fff;box-shadow:0 0 10px rgba(0,0,0,.35);overflow:hidden;z-index:5}
.mini .m{position:absolute}
.mini .t{font-size:4px;line-height:5px;color:#555}
.mini .h{font-size:4.5px;font-weight:700;color:var(--title);text-align:center;width:190px;left:0}
.mini .hw{font-size:4.5px;font-weight:700;color:#fff;text-align:center;width:190px;left:0}
.mini .rb{position:absolute;background:var(--red);color:#fff;font-size:3px;display:flex;align-items:center;justify-content:center}
.mini .card{position:absolute;background:#fff;border:.5px solid #ddd}
</style>
</head>
<body>
<div class="canvas">

  <!-- HOW YOU CAN HELP -->
  <section class="a help-band" aria-label="How you can help"></section>
  <div class="a brand-box"><div class="dot"></div><span>ALLIES OF<br>BEIT NOAM</span></div>
  <h2 class="a band-title" style="left:249px;top:33px">HOW YOU CAN HELP</h2>

  <div class="help-card" style="left:38px;top:88px;width:31px;height:180px">
    <div class="photo" role="img" aria-label="Wheelchair photo" style="left:0;top:0;width:31px;height:82px;background:linear-gradient(#8b93c4,#5d67a6)"></div>
    <p style="position:absolute;right:16px;top:92px">pair</p>
  </div>
  <div class="help-card" style="left:87px;top:88px;width:134px;height:180px">
    <div class="photo" role="img" aria-label="Child with headphones at home" style="left:0;top:0;width:134px;height:82px;background:linear-gradient(135deg,#c9b9ae,#8f93b3)"></div>
    <p style="position:absolute;left:0;top:91px;width:134px">Provides homebound<br>services for a year</p>
    <div class="price" style="position:absolute;top:121px;width:134px">$55.00</div>
    <div class="btn-red" style="left:36px;top:148px;width:64px;height:25px;font-size:9px;background:#b21f35">Donate</div>
  </div>
  <div class="help-card active" style="left:244px;top:77px;width:151px;height:199px">
    <div class="photo" role="img" aria-label="Oxygen mask and tubing" style="left:0;top:0;width:151px;height:94px;background:linear-gradient(135deg,#e4f3f3,#9fd3d3)"></div>
    <p style="position:absolute;left:0;top:101px;width:151px;font-size:10.5px;line-height:14px">Purchases an oxygen tank<br>and accessories</p>
    <div class="price" style="position:absolute;top:134px;width:151px;font-size:14px">$100.00</div>
    <div class="btn-red" style="left:40px;top:162px;width:72px;height:28px;font-size:10px">Donate</div>
  </div>
  <div class="help-card" style="left:414px;top:88px;width:99px;height:180px">
    <div class="photo" role="img" aria-label="Wheelchair photo" style="left:0;top:0;width:99px;height:82px;background:linear-gradient(135deg,#9aa0c8,#5e67a5)"></div>
    <p style="position:absolute;left:12px;top:91px;white-space:nowrap;text-align:left">Purchases an oxyge<br>and accessories</p>
    <div class="price" style="position:absolute;left:12px;top:121px">$250.00</div>
    <div class="btn-red" style="left:36px;top:148px;width:64px;height:25px;font-size:9px;background:#b21f35">Donate</div>
  </div>
  <div class="a dots"><i></i><i></i><i class="on"></i><i></i><i></i></div>

  <!-- IMPACT -->
  <section class="a impact-zone" aria-label="The impact of your support"></section>
  <h2 class="a sec-title" style="left:205px;top:360px">THE IMPACT OF YOUR SUPPORT</h2>

  <article class="impact-card" style="left:150px">
    <div class="photo" role="img" aria-label="Framed four-star charity rating certificate" style="left:12px;top:7px;width:141px;height:106px;background:linear-gradient(#f3f6f1,#e3ece4);border:4px solid #2f7d5c"></div>
    <div class="date">14 February 2021</div>
    <h3>4-stars for 9 years</h3>
    <p>This November, Allies of Beit Noam was rated a 4-star charity by Giving Ledger for the 9th consecutive year!</p>
    <div class="btn-line" style="left:91px;top:194px;width:61px;height:20px;font-size:8px">Read More</div>
  </article>
  <article class="impact-card" style="left:331px">
    <div class="photo" role="img" aria-label="Volunteer portrait with headline graphic about people helped every year" style="left:12px;top:7px;width:141px;height:106px;background:linear-gradient(120deg,#2f3e8e,#c73543 60%,#2b3a8a)"></div>
    <div class="date">19 July 2017</div>
    <h3>Beit Noam's Vital Statistics</h3>
    <p>This November, Allies of Beit Noam was rated a 4-star charity by Giving Ledger for the 9th consecutive year!</p>
    <div class="btn-line" style="left:92px;top:194px;width:61px;height:20px;font-size:8px">Read More</div>
  </article>

  <h2 class="a sec-title" style="left:221px;top:674px">THE LATEST AT BEIT NOAM</h2>
  <div class="photo" role="img" aria-label="Newsletter cover with two volunteers" style="left:153px;top:715px;width:102px;height:102px;background:linear-gradient(#3a6fb0,#b98f6f 55%,#2d6db0)"></div>
  <div class="a news" style="left:269px;top:720px;width:225px">
    <div class="date">14 February 2021</div>
    <h3 style="margin-top:5px">Inside Beit Noam - Fall 2022 Newsletter Is Here</h3>
    <p style="margin-top:6px">We are proud to bring you another edition of "INSIDE Beit Noam." We all know that the "inside" is what really counts – and here, that's a heart overflowing with compassion and action t...</p>
  </div>
  <div class="btn-line" style="left:269px;top:797px;width:61px;height:20px;font-size:8px">Read More</div>
  <div class="photo" role="img" aria-label="Volunteers assisting a visitor" style="left:153px;top:840px;width:102px;height:40px;background:linear-gradient(#8a7a6a,#b8a58e)"></div>
  <div class="a news" style="left:269px;top:846px;width:225px">
    <div class="date">04 July 2022</div>
    <h3 style="margin-top:5px">Beit Noam Assists Tourists of all Abilities</h3>
  </div>

  <!-- STATS -->
  <section class="a stats-band" aria-label="Services change lives"></section>
  <h2 class="a band-title" style="left:703px;top:35px;width:390px;text-align:center">BEIT NOAM'S SERVICES CHANGE LIVES</h2>
  <p class="a" style="left:703px;top:57px;width:390px;text-align:center;color:#fff;font-size:9.5px">Below are some of Beit Noam's Annual Figures</p>
  <div class="stat" style="left:724px"><div class="ring"><svg width="16" height="16" viewBox="0 0 16 16"><circle cx="8" cy="5" r="3.3" fill="#fff"/><path d="M2 15c0-4 3-6 6-6s6 2 6 6z" fill="#fff"/></svg></div><b>7,000</b><small>Volunteers</small></div>
  <div class="stat" style="left:809px"><div class="ring"><svg width="16" height="16" viewBox="0 0 16 16"><circle cx="8" cy="5" r="3.3" fill="#fff"/><path d="M2 15c0-4 3-6 6-6s6 2 6 6z" fill="#fff"/></svg></div><b>122</b><small>Branches</small></div>
  <div class="stat" style="left:895px"><div class="ring"><svg width="16" height="16" viewBox="0 0 16 16"><circle cx="8" cy="5" r="3.3" fill="#fff"/><path d="M2 15c0-4 3-6 6-6s6 2 6 6z" fill="#fff"/></svg></div><b>509,608</b><small>Medical Equipment<br>Loans</small></div>
  <div class="stat" style="left:980px"><div class="ring"><svg width="16" height="16" viewBox="0 0 16 16"><circle cx="8" cy="5" r="3.3" fill="#fff"/><path d="M2 15c0-4 3-6 6-6s6 2 6 6z" fill="#fff"/></svg></div><b>69,909</b><small>Phone Conversations<br>with Homebound</small></div>
  <div class="stat" style="left:1066px"><div class="ring"><svg width="16" height="16" viewBox="0 0 16 16"><circle cx="8" cy="5" r="3.3" fill="#fff"/><path d="M2 15c0-4 3-6 6-6s6 2 6 6z" fill="#fff"/></svg></div><b>297,564</b><small>Calls to Emergency<br>Hotline</small></div>

  <!-- ABOUT / SUPPORT / PROFILE -->
  <section class="a info-zone" aria-label="About us and profile"></section>
  <h2 class="a sec-title" style="left:683px;top:255px;font-size:14px">ABOUT US</h2>
  <p class="a body-text" style="left:683px;top:283px;width:210px">Beit Noam is Israel's largest volunteer-staffed organization providing a wide array of compassionate health and home care services for people of all ages, with special programs directed at support for older adults and for children and adults with disabilities.</p>
  <div class="btn-red" style="left:690px;top:377px;width:58px;height:19px;font-size:8.5px;text-transform:none;font-weight:400">Read More</div>
  <h2 class="a sec-title" style="left:939px;top:255px;font-size:14px">SUPPORT US</h2>
  <p class="a body-text" style="left:939px;top:284px;width:180px">Your gift will help provide a vital array of compassionate health and home care services for people of all ages in Israel!</p>
  <div class="btn-red" style="left:939px;top:338px;width:61px;height:19px;font-size:8.5px;text-transform:none;font-weight:400">Read More</div>
  <h2 class="a sec-title" style="left:851px;top:442px;font-size:14px">OUR PROFILE</h2>
  <div class="a" role="img" aria-label="Transparency seal" style="left:762px;top:482px;width:44px;height:44px;border-radius:50%;background:#e9b94a;border:3px solid #fff"></div>
  <p class="a body-text" style="left:830px;top:486px;width:230px;font-size:8.5px">ClearGive revolutionizes philanthropy by providing information that advances transparency so donors can make better decisions.</p>
  <div class="a" role="img" aria-label="Rating certificate" style="left:758px;top:557px;width:52px;height:41px;background:#eef3ee;border:3px solid #3a8a6a"></div>
  <p class="a body-text" style="left:830px;top:560px;width:200px;font-size:8.5px">Allies of Beit Noam has earned a Beit Noam ClearGive 2020 ninth consecutive 4-star rating from Giving Ledger.</p>

  <!-- FOOTER -->
  <footer class="a footer"></footer>
  <div class="a" style="left:720px;top:688px;display:flex;align-items:center;gap:7px">
    <div style="width:24px;height:24px;border-radius:50%;background:var(--red)"></div>
    <span style="color:#fff;font-weight:700;font-size:12px;line-height:13px">ALLIES OF<br>BEIT NOAM</span>
  </div>
  <div class="social" style="left:719px"></div><div class="social" style="left:741px"></div><div class="social" style="left:763px"></div><div class="social" style="left:785px"></div><div class="social" style="left:807px"></div><div class="social" style="left:829px"></div>
  <nav class="a foot-nav">
    <a href="#" style="margin-right:14px">Home</a><a href="#" style="margin-right:14px">About Us</a><a href="#">Our Impact</a><br>
    <a href="#" style="margin-right:4px">Newsroom</a><a href="#" style="margin-right:4px">Contact Us</a><a href="#">Get Involved</a><br>
    <a href="#" style="margin-right:4px">Privacy Policy</a><a href="#">State Nonprofit Disclosures</a>
  </nav>
  <svg class="a" style="left:736px;top:785px" width="11" height="11" viewBox="0 0 24 24"><path fill="#fff" d="M6.6 10.8a15 15 0 006.6 6.6l2.2-2.2c.3-.3.7-.4 1-.2 1.1.4 2.3.6 3.6.6.6 0 1 .4 1 1V20c0 .6-.4 1-1 1A17 17 0 013 4c0-.6.4-1 1-1h3.5c.6 0 1 .4 1 1 0 1.3.2 2.5.6 3.6.1.3 0 .7-.2 1z"/></svg>
  <p class="a center" style="left:700px;top:806px;width:80px;color:#fff;font-size:8px;line-height:13px">212.555.0147<br>866.555.0199</p>
  <svg class="a" style="left:889px;top:784px" width="11" height="13" viewBox="0 0 24 28"><path fill="#fff" d="M12 0a9 9 0 00-9 9c0 7 9 19 9 19s9-12 9-19a9 9 0 00-9-9zm0 12.5A3.5 3.5 0 1112 5.5a3.5 3.5 0 010 7z"/></svg>
  <p class="a center" style="left:800px;top:806px;width:190px;color:#fff;font-size:8px;line-height:13px">Allies of Beit Noam,Inc., 120 Harbor Street,<br>Suite 410, New York, NY 10010 USA</p>
  <svg class="a" style="left:1041px;top:786px" width="12" height="9" viewBox="0 0 24 18"><path fill="#fff" d="M0 0h24v18H0z"/><path d="M0 0l12 9 12-9" fill="none" stroke="#0b1a7f" stroke-width="2"/></svg>
  <p class="a center" style="left:975px;top:806px;width:145px;color:#fff;font-size:8px">shalom@alliesofbeitnoam.org</p>
  <p class="a center" style="left:703px;top:857px;width:382px;color:#fff;font-size:7px">Copyright© 2023 Allies of Beit Noam, All rights reserved. Bringing Help and Hope to the People of Israel.</p>

  <!-- HOMEPAGE OVERVIEW -->
  <div class="a mini" aria-label="Full homepage overview">
    <div class="m" style="left:0;top:0;width:190px;height:21px;background:#fff"></div>
    <div class="m" style="left:22px;top:6px;width:7px;height:7px;border-radius:50%;background:var(--red)"></div>
    <div class="m" style="left:31px;top:6px;font-size:3.5px;font-weight:700;color:var(--title);line-height:4px">ALLIES OF<br>BEIT NOAM</div>
    <div class="m t" style="left:68px;top:8px;font-size:3.3px;color:var(--title)">Home&nbsp;&nbsp;About Us&nbsp;&nbsp;Newsroom&nbsp;&nbsp;Contact Us&nbsp;&nbsp;Get Involved</div>
    <div class="rb" style="left:167px;top:6px;width:17px;height:7px">DONATE</div>

    <div class="m" role="img" aria-label="Portrait of an older woman beside a historic photo" style="left:0;top:21px;width:190px;height:69px;background:linear-gradient(90deg,#c7414f,#d9848a 55%,#b7a9b0)"></div>
    <div class="m" style="left:17px;top:38px;font-size:5px;font-weight:700;color:#fff;line-height:6px">TOGETHER WE CAN HELP<br>ISRAEL'S BUILDERS.</div>
    <div class="m" style="left:17px;top:52px;font-size:3.2px;color:#fff">Now and for the next 75 years</div>
    <div class="rb" style="left:17px;top:64px;width:33px;height:6px">MAKE A DONATION</div>

    <div class="m" style="left:0;top:90px;width:190px;height:128px;background:linear-gradient(#eef0f7,#f2e6ee)"></div>
    <div class="m h" style="top:107px">HOW WE CARE FOR ISRAEL'S BUILDERS</div>
    <div class="m" role="img" aria-label="Video about caring for older people" style="left:26px;top:120px;width:140px;height:79px;background:linear-gradient(135deg,#cfc7cf,#8e8aa3)"></div>
    <div class="m" style="left:85px;top:152px;width:14px;height:10px;border-radius:2px;background:var(--red)"></div>

    <div class="m" style="left:0;top:218px;width:190px;height:110px;background:var(--blue)"></div>
    <div class="m hw" style="top:229px">HOW YOU CAN HELP</div>
    <div class="card" style="left:0;top:247px;width:38px;height:57px;opacity:.8"></div>
    <div class="card" style="left:15px;top:247px;width:48px;height:57px;opacity:.85"><div class="m" style="left:0;top:0;width:48px;height:25px;background:#b9aeb0"></div><div class="m t" style="left:2px;top:28px;width:44px;text-align:center;font-size:3px;line-height:4px">Provides homebound services for a year</div><div class="rb" style="left:12px;top:46px;width:24px;height:6px">DONATE</div></div>
    <div class="card" style="left:69px;top:243px;width:52px;height:65px"><div class="m" style="left:0;top:0;width:52px;height:30px;background:#bfe3e3"></div><div class="m t" style="left:2px;top:33px;width:48px;text-align:center;font-size:3.2px;line-height:4px">Purchases an oxygen tank and accessories</div><div class="m" style="left:0;top:43px;width:52px;text-align:center;color:var(--red);font-weight:700;font-size:4px">$100.00</div><div class="rb" style="left:14px;top:52px;width:24px;height:7px">DONATE</div></div>
    <div class="card" style="left:127px;top:247px;width:48px;height:57px;opacity:.85"><div class="m" style="left:0;top:0;width:48px;height:25px;background:#9aa0c2"></div><div class="m t" style="left:2px;top:28px;width:44px;text-align:center;font-size:3px;line-height:4px">Purchases an oxygen tank and accessories</div><div class="rb" style="left:12px;top:46px;width:24px;height:6px">DONATE</div></div>
    <div class="m" style="left:86px;top:318px;font-size:4px;color:#fff;letter-spacing:1px">• • ● • •</div>

    <div class="m" style="left:0;top:328px;width:190px;height:220px;background:linear-gradient(#eceaf3,#f3e2e8)"></div>
    <div class="m h" style="top:336px">THE IMPACT OF YOUR SUPPORT</div>
    <div class="card" style="left:38px;top:349px;width:51px;height:75px"><div class="m" style="left:3px;top:3px;width:45px;height:33px;background:#e3ece4;border:1px solid #3a8a6a"></div><div class="m" style="left:3px;top:40px;font-size:3.2px;color:var(--red)">4-stars for 9 years</div><div class="m t" style="left:3px;top:45px;width:45px;font-size:2.6px;line-height:3.2px">Rated a 4-star charity for the 9th year in a row by the Ledger.</div></div>
    <div class="card" style="left:100px;top:349px;width:51px;height:75px"><div class="m" style="left:3px;top:3px;width:45px;height:33px;background:linear-gradient(120deg,#2f3e8e,#c73543)"></div><div class="m" style="left:3px;top:40px;font-size:3.2px;color:var(--red)">Vital Statistics</div><div class="m t" style="left:3px;top:45px;width:45px;font-size:2.6px;line-height:3.2px">Rated a 4-star charity for the 9th year in a row by the Ledger.</div></div>
    <div class="m h" style="top:440px">THE LATEST AT BEIT NOAM</div>
    <div class="m" role="img" aria-label="Newsletter cover" style="left:38px;top:453px;width:34px;height:34px;background:linear-gradient(#3a6fb0,#b98f6f)"></div>
    <div class="m" style="left:77px;top:459px;font-size:3.3px;color:var(--red)">Inside Beit Noam - Fall 2022 Newsletter Is Here</div>
    <div class="m t" style="left:77px;top:464px;width:80px;font-size:2.6px;line-height:3.2px">We are proud to bring you another edition of our newsletter, full of stories of care.</div>
    <div class="m" role="img" aria-label="Volunteers with a visitor" style="left:38px;top:495px;width:34px;height:34px;background:linear-gradient(#8a7a6a,#b8a58e)"></div>
    <div class="m" style="left:77px;top:500px;font-size:3.3px;color:var(--red)">Beit Noam Assists Tourists of all Abilities</div>
    <div class="m t" style="left:77px;top:505px;width:80px;font-size:2.6px;line-height:3.2px">Visitors with limited mobility can borrow equipment to enjoy their trip.</div>

    <div class="m" style="left:0;top:548px;width:190px;height:68px;background:var(--blue)"></div>
    <div class="m hw" style="top:555px">BEIT NOAM'S SERVICES CHANGE LIVES</div>
    <div class="m" style="left:0;top:561px;width:190px;text-align:center;font-size:3px;color:#fff">Below are some of Beit Noam's Annual Figures</div>
    <div class="m" style="left:15px;top:571px;width:160px;display:flex;justify-content:space-between">
      <i style="width:9px;height:9px;border-radius:50%;border:.6px solid #fff"></i><i style="width:9px;height:9px;border-radius:50%;border:.6px solid #fff"></i><i style="width:9px;height:9px;border-radius:50%;border:.6px solid #fff"></i><i style="width:9px;height:9px;border-radius:50%;border:.6px solid #fff"></i><i style="width:9px;height:9px;border-radius:50%;border:.6px solid #fff"></i><i style="width:9px;height:9px;border-radius:50%;border:.6px solid #fff"></i>
    </div>
    <div class="m" style="left:10px;top:584px;width:172px;display:flex;justify-content:space-between;font-size:3px;color:#fff;font-weight:700"><span>800,000</span><span>7,000</span><span>122</span><span>509,608</span><span>69,909</span><span>297,564</span></div>

    <div class="m" style="left:0;top:616px;width:190px;height:144px;background:linear-gradient(#ecebf4,#f2e4ea)"></div>
    <div class="m" style="left:24px;top:629px;font-size:3.8px;font-weight:700;color:var(--title)">ABOUT US</div>
    <div class="m t" style="left:24px;top:636px;width:70px;font-size:2.8px;line-height:3.5px">Beit Noam is Israel's largest volunteer-staffed group providing a wide array of caring health and home services for people of all ages, with programs for older adults and for children and adults with disabilities.</div>
    <div class="rb" style="left:24px;top:669px;width:19px;height:5px">Read More</div>
    <div class="m" style="left:109px;top:629px;font-size:3.8px;font-weight:700;color:var(--title)">SUPPORT US</div>
    <div class="m t" style="left:109px;top:636px;width:65px;font-size:2.8px;line-height:3.5px">Your gift will help provide a vital array of caring health and home services for all ages in Israel!</div>
    <div class="rb" style="left:109px;top:656px;width:19px;height:5px">Read More</div>
    <div class="m h" style="top:690px;font-size:3.8px">OUR PROFILE</div>
    <div class="m" style="left:54px;top:703px;width:10px;height:10px;border-radius:50%;background:#e9b94a"></div>
    <div class="m t" style="left:70px;top:705px;width:70px;font-size:2.6px;line-height:3.2px">ClearGive shares data that helps donors make better choices.</div>
    <div class="m" style="left:51px;top:728px;width:14px;height:11px;background:#eef3ee;border:.8px solid #3a8a6a"></div>
    <div class="m t" style="left:70px;top:730px;width:70px;font-size:2.6px;line-height:3.2px">Ninth consecutive 4-star rating from Giving Ledger.</div>

    <div class="m" style="left:0;top:760px;width:190px;height:75px;background:var(--navy)"></div>
    <div class="m" style="left:36px;top:772px;width:6px;height:6px;border-radius:50%;background:var(--red)"></div>
    <div class="m" style="left:44px;top:771px;font-size:3.3px;font-weight:700;color:#fff;line-height:4px">ALLIES OF<br>BEIT NOAM</div>
    <div class="m" style="left:36px;top:785px;font-size:3px;color:#fff;letter-spacing:1px">○○○○○○</div>
    <div class="m" style="left:108px;top:772px;font-size:2.6px;color:#fff;line-height:4px">Home&nbsp; About Us&nbsp; Our Impact<br>Newsroom&nbsp; Contact Us&nbsp; Get Involved<br>Privacy Policy&nbsp; Disclosures</div>
    <div class="m" style="left:0;top:802px;width:190px;display:flex;justify-content:space-around;font-size:2.4px;color:#fff;text-align:center">
      <span>212.555.0147<br>866.555.0199</span><span>120 Harbor Street, Suite 410<br>New York, NY 10010 USA</span><span>shalom@alliesofbeitnoam.org</span>
    </div>
    <div class="m" style="left:0;top:825px;width:190px;text-align:center;font-size:2.2px;color:#fff">Copyright© 2023 Allies of Beit Noam. All rights reserved.</div>
  </div>

</div>
</body>
</html>
```